Human Resources Flyer design

Create a 1 page flyer design for a staffing company that is looking to provide its services to clients. Images centered around people and businesses.
Target Market(s)
Large businesses
Industry/Entity Type
Staffing
Requirements
Must have
- Use color scheme that matches norvelhire.example.
Nice to have
- Flow chart like image for 3 areas mentioned.
- Images that convey professionalism and people connections

```html
<!DOCTYPE html>
<html lang="en">
<head>
<meta charset="utf-8">
<title>Norvel Hire – Flyer</title>
<link rel="stylesheet" href="https://fonts.googleapis.com/css2?family=Montserrat:wght@400;500;600;700&display=swap">
<style>
  :root {
    --navy: #1e2836;
    --navy-mid: #2b3d57;
    --navy-soft: #3f5878;
    --red: #d31c42;
    --ink: #3d424a;
    --ink-soft: #6b717a;
    --paper: #fbfbfc;
    --stage: #e3e4e6;
    --rule: #c9ccd1;
  }
  * { box-sizing: border-box; margin: 0; padding: 0; }
  html, body { width: 1200px; height: 796px; overflow: hidden; }
  body {
    background: var(--stage);
    font-family: "Montserrat", Arial, sans-serif;
    color: var(--ink);
  }
  .flyer {
    position: absolute;
    left: 305px; top: 16px;
    width: 590px; height: 764px;
    background: var(--paper);
    box-shadow: 0 6px 22px rgba(0,0,0,.18);
    overflow: hidden;
  }
  .banner { position: absolute; left: 0; top: 0; width: 100%; height: 62px; display: flex; gap: 3px; background: var(--navy); }
  .banner-photo { flex: 1; }
  .banner-photo.one { background: linear-gradient(135deg, #1f3350, #3a5577); }
  .banner-photo.two { background: linear-gradient(135deg, #2e4a6c, #5f7591 60%, #8a8f5a); }
  .banner-photo.three { background: linear-gradient(135deg, #23344d, #45617f); }

  .brand { position: absolute; left: 40px; top: 80px; display: flex; align-items: center; gap: 8px; }
  .brand-mark { width: 14px; height: 14px; background: var(--navy); }
  .brand-name { font-size: 20px; font-weight: 600; letter-spacing: 3px; color: var(--navy); }

  .intro { position: absolute; left: 40px; top: 112px; width: 360px; font-size: 6.8px; line-height: 1.45; color: var(--ink-soft); }

  .headline { position: absolute; left: 110px; top: 150px; width: 300px; }
  .headline h1 { font-size: 13px; font-weight: 500; color: #7b8089; white-space: nowrap; line-height: 1.2; }
  .headline p { margin-top: 4px; font-size: 9px; font-weight: 600; color: var(--navy-mid); line-height: 1.3; }

  .art { position: absolute; left: 0; top: 0; }

  .tag { position: absolute; color: #fff; font-size: 9px; font-weight: 600; text-align: center; line-height: 1.2; padding: 5px 8px; }
  .tag.dark { background: var(--navy); }
  .tag.red { background: var(--red); }

  .stage { position: absolute; font-size: 7px; line-height: 1.45; }
  .stage .desc { color: var(--ink-soft); margin-bottom: 10px; }
  .stage ul { list-style: none; }
  .stage li { font-size: 8px; font-weight: 500; color: var(--navy-mid); margin-bottom: 7px; line-height: 1.3; }

  .stage.tactical { left: 34px; top: 392px; width: 182px; }
  .stage.supervisor { left: 236px; top: 376px; width: 152px; }
  .stage.business { left: 408px; top: 244px; width: 160px; }

  .footer {
    position: absolute; left: 0; bottom: 0; width: 100%; height: 78px;
    background: var(--navy); color: #fff;
    display: flex; justify-content: space-between; align-items: center;
    padding: 0 32px;
  }
  .footer-address { font-size: 7px; line-height: 1.6; color: #aeb6c2; }
  .footer-contact { text-align: right; }
  .footer-phone { font-size: 26px; font-weight: 700; letter-spacing: .5px; }
  .footer-email { font-size: 8px; color: #c7ced8; margin-top: 2px; }
</style>
</head>
<body>
  <main class="flyer">
    <header class="banner">
      <div class="banner-photo one" role="img" aria-label="Photo of business professionals at work in blue tones"></div>
      <div class="banner-photo two" role="img" aria-label="Photo of an office team meeting in blue tones"></div>
      <div class="banner-photo three" role="img" aria-label="Photo of a city business district in blue tones"></div>
    </header>

    <div class="brand">
      <span class="brand-mark"></span>
      <span class="brand-name">NORVEL HIRE</span>
    </div>

    <p class="intro">Norvel Hire combines the best tools in human resource and risk management with industry-leading knowledge to create a unique operational platform. Our specialists handle workforce administration, compensation oversight and safety programs, giving our clients the structure to grow their own business.</p>

    <div class="headline">
      <h1>What you can expect from Norvel Hire</h1>
      <p>Business owners working with Norvel Hire<br>typically move through three stages</p>
    </div>

    <svg class="art" width="590" height="690" viewBox="0 0 590 690">
      <defs>
        <linearGradient id="photoWarm" x1="0" y1="0" x2="1" y2="1">
          <stop offset="0" stop-color="#e9edf2"/>
          <stop offset="1" stop-color="#9fb2c8"/>
        </linearGradient>
        <linearGradient id="photoOffice" x1="0" y1="0" x2="1" y2="1">
          <stop offset="0" stop-color="#dfe6ee"/>
          <stop offset="1" stop-color="#4a6483"/>
        </linearGradient>
      </defs>

      <!-- business level guidance -->
      <path d="M 420 118 A 56 56 0 1 1 440 190" fill="none" stroke="var(--red)" stroke-width="3"/>
      <polygon points="412,124 424,112 428,128" fill="var(--red)"/>
      <circle cx="470" cy="140" r="42" fill="url(#photoWarm)" stroke="var(--red)" stroke-width="6" role="img" aria-label="Photo of smiling colleagues shaking hands"/>
      <line x1="470" y1="196" x2="485" y2="214" stroke="var(--navy)" stroke-width="1.2" stroke-dasharray="2 2"/>

      <!-- supervisor development -->
      <circle cx="300" cy="272" r="58" fill="none" stroke="var(--navy)" stroke-width="2"/>
      <circle cx="300" cy="272" r="44" fill="url(#photoOffice)" stroke="var(--navy)" stroke-width="8" role="img" aria-label="Photo of two business people greeting in an office"/>
      <line x1="300" y1="330" x2="300" y2="342" stroke="var(--navy)" stroke-width="1.2" stroke-dasharray="2 2"/>

      <!-- tactical alignment -->
      <path d="M 70 318 A 54 54 0 1 1 165 316" fill="none" stroke="var(--navy)" stroke-width="2"/>
      <polygon points="135,234 125,229 126,240" fill="var(--navy)"/>
      <circle cx="115" cy="290" r="38" fill="url(#photoWarm)" stroke="var(--navy)" stroke-width="6" role="img" aria-label="Photo of a team working together at a desk"/>
      <line x1="115" y1="344" x2="115" y2="356" stroke="var(--navy)" stroke-width="1.2" stroke-dasharray="2 2"/>

      <!-- column rules -->
      <line x1="226" y1="392" x2="226" y2="660" stroke="var(--rule)" stroke-width="0.8"/>
      <line x1="398" y1="250" x2="398" y2="580" stroke="var(--rule)" stroke-width="0.8"/>
      <line x1="34" y1="386" x2="216" y2="386" stroke="var(--rule)" stroke-width="0.8"/>
      <line x1="408" y1="236" x2="568" y2="236" stroke="var(--rule)" stroke-width="0.8"/>
    </svg>

    <div class="tag red" style="left:420px; top:212px; width:132px;">Business<br>level guidance</div>
    <div class="tag dark" style="left:246px; top:342px; width:108px;">Supervisor<br>Development</div>
    <div class="tag dark" style="left:58px; top:356px; width:114px;">Tactical Alignment</div>

    <section class="stage business">
      <p class="desc">Activities involved in the third stage of the relationship are more strategic and forward looking, with a goal of cultivating an environment in your organization in which employees and supervisors drive the success of the organization instead of just the business owner. Areas of focus may include:</p>
      <ul>
        <li>Strategic planning</li>
        <li>Proactive mitigation of business risks</li>
        <li>Holistic view of where your business is going</li>
        <li>Leadership development and succession planning</li>
        <li>Organizational development and design</li>
      </ul>
    </section>

    <section class="stage supervisor">
      <p class="desc">The second stage of the relationship focuses on furthering process improvements, further development of HR roles and a pathway to supervisor development. Areas of focus include:</p>
      <ul>
        <li>Ongoing development and refinement of action plans</li>
        <li>Supervisory skill development and training for workplace safety</li>
        <li>Effective human capital management and overall risk mitigation</li>
        <li>Platform for performance management and performance improvement</li>
        <li>Evaluation of employee benefits options</li>
      </ul>
    </section>

    <section class="stage tactical">
      <p class="desc">The first stage addresses the administrative and tactical components of managing your employees.</p>
      <ul>
        <li>Analysis of safety programs and HR practices</li>
        <li>Establish payroll submission and administration protocol</li>
        <li>Hiring, selection and new hire onboarding best practices</li>
        <li>Injury reporting protocol</li>
        <li>Establishing goals and creation of action plan</li>
        <li>Identification of metrics to track effectiveness</li>
      </ul>
    </section>

    <footer class="footer">
      <div class="footer-address">
        418 Harbor Line Ave, Ste 7, Lakeview, CA 90000<br>
        Office: 555-014-2290<br>
        Hours: 8:00 a.m. – 5:00 p.m. M–F
      </div>
      <div class="footer-contact">
        <div class="footer-phone">555-014-2290</div>
        <div class="footer-email">info@norvelhire.example</div>
      </div>
    </footer>
  </main>
</body>
</html>
```